Business cards, envelopes, etc. for real estate company

We have a finished logo for our real estate company. We need a corporate identity package with the following items:

1. Business Cards
2. Letterhead/Stationary - with 2 pages:
-1st page with full header
-2nd page without top header
3. Concise and professional e-mail signature image
4. Fax coversheet
5. Shipping label, with our return address and a mail-to address (on one label)

We need these to be editable. We don't know the industry standard for these items but perhaps you can provide them to us in .PDF and Word format (and if you use Adobe Illustrator for them, .AI as well).

Please use the attached placeholder logo in your design entry. We will provide you with the original logo to swap in (same size and design, just different text) when we choose your entry.

Please include the following information on the letterhead and business cards:

58 Birchwell Road
Suite 2B West
New York, NY 10587

Tel: 555-014-2837
Fax :555-014-2837

Please contact us if you have any questions about this contest.

Hi,

Thanks for your interest in this project. The logo to use should be working now. Please contact me if you have any further issues or questions.

I look forward to seeing your submissions. 

Hi,

We first wish to thank you all for your submissions. 

Here is some general feedback regarding the designs shown:

1. We would prefer square (as opposed to rounded) business cards.

2. For the fax coversheets, we are looking with a designed look. While we understand these are samples, we don't want it to appear as if it a standard block of text or a fax template from a word processing program.

3. For the 1st page of letterhead and envelopes, we do need an office address on them. The envelopes should have space for a stamp in the top right corner. We would prefer the envelopes not to have colored stripes.

4. We think a watermark of the logo is an interesting idea on the business cards and/or letterhead. This may be something to try. However, it is not strictly necessary and we would like to evaluate designs with and without it.

In general we are looking for a clean yet professional look.

We are actively reviewing all entries and thank you for your time and creativity.

One last comment: We understand making all objects in the brief takes some time. However, we want to remind all the designers that this contest is for more than just business cards (envelopes, letterheads, etc.) so if we choose your design, those items will be expected. Please refer to the original brief to see what we are requesting.

If you provide a mockup of any item listed in the brief (in addition to business cards) it would help us visualize your entire vision for this project.

```html
<!DOCTYPE html>
<html lang="en">
<head>
<meta charset="utf-8">
<title>Halden &amp; Halden – Business Card</title>
<link rel="stylesheet" href="https://fonts.googleapis.com/css2?family=Ubuntu:wght@400;500&display=swap">
<style>
  :root {
    --teal: #234b5c;
    --teal-light: #5f8797;
    --grey-text: #7a7f83;
    --card-white: #ffffff;
    --backdrop: #d9dadb;
  }
  * { margin: 0; padding: 0; box-sizing: border-box; }
  html, body { width: 1200px; height: 960px; overflow: hidden; }
  body {
    background: var(--backdrop);
    font-family: "Ubuntu", "Helvetica Neue", Arial, sans-serif;
    position: relative;
  }
  .card {
    position: absolute;
    left: 250px;
    width: 700px;
    height: 400px;
    border-radius: 34px;
    overflow: hidden;
    box-shadow: 0 10px 28px rgba(0,0,0,0.18);
  }
  .card-front { top: 50px; background: var(--card-white); }
  .card-back {
    top: 505px;
    background: linear-gradient(100deg, var(--teal) 0%, var(--teal) 45%, var(--teal-light) 72%, #3d6576 88%, var(--teal) 100%);
  }
  .card-front .sheen {
    position: absolute; right: 0; top: 0; width: 260px; height: 260px;
    background: radial-gradient(ellipse at 90% 0%, #eceeef 0%, rgba(255,255,255,0) 70%);
  }
  .holder { position: absolute; left: 68px; top: 60px; }
  .holder-name { color: var(--teal); font-size: 38px; font-weight: 400; line-height: 1.1; }
  .holder-title { color: var(--grey-text); font-size: 24px; margin-top: 4px; }
  .contact {
    position: absolute; left: 68px; top: 196px;
    font-style: normal;
    color: var(--grey-text); font-size: 20px; line-height: 1.3;
  }
  .contact .company { color: var(--teal); }
  .contact .phones { margin-top: 8px; color: var(--teal); }
  .contact .phones span { color: var(--grey-text); }
  .brand {
    position: absolute; display: flex; align-items: center; gap: 14px;
  }
  .brand-mark { width: 66px; height: 66px; flex: none; }
  .brand-name { font-size: 36px; line-height: 1.05; font-weight: 400; }
  .card-front .brand { left: 400px; top: 232px; }
  .card-front .brand-mark { background: var(--teal); }
  .card-front .brand-name { color: var(--grey-text); }
  .card-back .brand { left: 120px; top: 160px; }
  .card-back .brand-mark { background: #ffffff; }
  .card-back .brand-name { color: #ffffff; font-size: 38px; }
</style>
</head>
<body>
  <section class="card card-front">
    <div class="sheen"></div>
    <div class="holder">
      <p class="holder-name">Your Name</p>
      <p class="holder-title">Your Designation</p>
    </div>
    <address class="contact">
      <p class="company">Halden &amp; Halden</p>
      <p>58 Birchwell Road</p>
      <p>Suite 2B West</p>
      <p>New York, NY 10587</p>
      <div class="phones">
        <p>Tel:&nbsp; <span>555-014-2837</span></p>
        <p>Fax: <span>555-014-2837</span></p>
      </div>
    </address>
    <div class="brand">
      <div class="brand-mark"></div>
      <p class="brand-name">Halden<br>&amp; Halden</p>
    </div>
  </section>

  <section class="card card-back">
    <div class="brand">
      <div class="brand-mark"></div>
      <p class="brand-name">Halden<br>&amp; Halden</p>
    </div>
  </section>
</body>
</html>
```